Brightfen Landscaping Folder Design

I need a graphic designer to design a folder so we can insert informational sheets inside it for customers. The folder must include the company logo, project images, on front and back of folder and slogan " The Experience You Want, The Service You Expect, And The Value You Deserve'

Folder to also include phone numbers : 647 392 5180 as well as the website: www.brightfenlandscaping.example as well as we gurantee a 24 month warranty.

I have attached sample of size we need.

Pixel Harbor has also done something similar for me for Juniper Yards

Target Market(s)

geared toward home owners & commercial/industrial

Industry/Entity Type

Landscaping

Font styles to use
Other font styles liked:
• open to new trendy font

Requirements
Must have
• Telephone Number, email address, slogan, images,
Nice to have
• images of completed projects incorporated into the front and back of folder as well as the logo
Should not have
• n/a

```html
<!DOCTYPE html>
<html lang="en">
<head>
<meta charset="utf-8">
<title>Brightfen Landscaping Folder</title>
<link rel="stylesheet" href="https://fonts.googleapis.com/css2?family=Montserrat:wght@400;500;600;700;800&display=swap">
<style>
  :root{
    --stage:#6a6a6a;
    --ink:#231f20;
    --blue:#1389f5;
    --blue-deep:#0d5fc4;
    --blue-mid:#1a74de;
    --grey-light:#f1f1f1;
    --text-dark:#3a3a3a;
    --brand-grey:#777777;
    --white:#ffffff;
  }
  html,body{margin:0;padding:0;overflow:hidden;}
  body{width:1200px;height:907px;background:var(--stage);position:relative;font-family:"Montserrat",sans-serif;}
  .folder{position:absolute;left:0;top:0;width:1200px;height:907px;}
  .folder-art{position:absolute;left:0;top:0;}
  .brand-name{position:absolute;font-weight:700;letter-spacing:0.5px;text-transform:uppercase;line-height:1.15;white-space:nowrap;}
  .brand-name--back{left:166px;top:599px;font-size:10px;color:var(--brand-grey);}
  .brand-name--front{left:617px;top:470px;font-size:12px;color:var(--white);}
  .brand-sub{display:block;font-size:7px;margin-left:14px;letter-spacing:1px;}
  .brand-name--front .brand-sub{font-size:8px;}
  .brand-mark{display:inline-block;width:8px;height:8px;background:currentColor;margin-right:6px;vertical-align:0;}
  .contact{position:absolute;font-size:8.5px;color:var(--text-dark);line-height:11px;font-weight:500;white-space:nowrap;}
  .contact--address{left:262px;top:600px;}
  .contact--lines{left:410px;top:600px;}
  .contact-row{display:flex;align-items:center;gap:5px;}
  .contact-indent{padding-left:12px;}
  .warranty{position:absolute;left:533px;top:530px;transform:translate(-50%,-50%) rotate(-8deg);display:flex;align-items:center;gap:3px;color:var(--white);font-weight:800;font-style:italic;line-height:1;white-space:nowrap;}
  .warranty-num{font-size:24px;letter-spacing:-0.5px;}
  .warranty-words{display:flex;flex-direction:column;font-size:12px;line-height:12px;}
  .slogan{position:absolute;left:615px;top:540px;color:var(--white);font-weight:500;margin:0;}
  .slogan span{display:block;white-space:nowrap;}
  .slogan .line-1{font-size:18px;line-height:26px;}
  .slogan .line-2,.slogan .line-3{font-size:21px;line-height:29px;}
</style>
</head>
<body>
<div class="folder">
  <svg class="folder-art" width="1200" height="907" viewBox="0 0 1200 907">
    <defs>
      <linearGradient id="pocketGrey" x1="0" x2="1" y1="0" y2="0">
        <stop offset="0" stop-color="#d6d6d6"/><stop offset="0.5" stop-color="#fafafa"/><stop offset="1" stop-color="#dedede"/>
      </linearGradient>
      <linearGradient id="pocketBlue" x1="0" x2="1" y1="0" y2="1">
        <stop offset="0" stop-color="#1877e6"/><stop offset="1" stop-color="#0b58c0"/>
      </linearGradient>
      <linearGradient id="drivePhoto" x1="0" x2="1" y1="0" y2="1">
        <stop offset="0" stop-color="#3e4a32"/><stop offset="0.5" stop-color="#a9aba5"/><stop offset="1" stop-color="#d8d8d4"/>
      </linearGradient>
      <linearGradient id="poolPhoto" x1="0" x2="0" y1="0" y2="1">
        <stop offset="0" stop-color="#5b5238"/><stop offset="0.45" stop-color="#2b6db8"/><stop offset="1" stop-color="#7e7870"/>
      </linearGradient>
      <linearGradient id="walkPhoto" x1="0" x2="1" y1="0" y2="1">
        <stop offset="0" stop-color="#4f6b3a"/><stop offset="1" stop-color="#a7a39a"/>
      </linearGradient>
    </defs>

    <rect class="panel-back" x="148" y="50" width="452" height="605" fill="var(--grey-light)"/>
    <polygon role="img" aria-label="Photo of a finished curved concrete driveway in front of a house" points="148,92 600,372 600,385 440,455 148,555" fill="url(#drivePhoto)"/>
    <polygon class="accent-blue" points="600,50 600,275 405,160" fill="var(--blue)"/>
    <polygon class="accent-grey" points="440,380 600,380 600,470 470,470" fill="#8b8b8b" opacity="0.7"/>

    <rect class="panel-front" x="600" y="50" width="456" height="605" fill="var(--blue-mid)"/>
    <polygon role="img" aria-label="Photo of a lit backyard pool with stone waterfall and patio" points="600,50 1056,50 1056,485 980,490 600,380" fill="url(#poolPhoto)"/>
    <polygon points="600,380 980,490 1056,485 1056,655 600,655" fill="var(--blue-mid)"/>
    <polygon points="600,470 1056,600 1056,655 600,655" fill="var(--blue-deep)" opacity="0.6"/>
    <polygon points="970,500 1056,450 1056,540" fill="var(--blue)"/>

    <polygon class="band" points="148,50 215,50 1056,575 1056,632 148,92" fill="var(--ink)"/>

    <rect x="416" y="386" width="92" height="92" rx="10" transform="rotate(45 462 432)" fill="var(--blue)"/>
    <rect role="img" aria-label="Photo of a paver walkway with garden steps" x="422" y="392" width="80" height="80" rx="8" transform="rotate(45 462 432)" fill="url(#walkPhoto)"/>

    <rect class="warranty-badge" x="489" y="486" width="88" height="88" rx="10" transform="rotate(45 533 530)" fill="var(--blue-deep)"/>
    <rect x="493" y="490" width="80" height="80" rx="8" transform="rotate(45 533 530)" fill="var(--blue)" opacity="0.6"/>

    <polygon class="pocket-back" points="148,655 600,655 600,835 592,852 148,852" fill="url(#pocketGrey)"/>
    <polygon class="pocket-front" points="600,655 1056,655 1056,852 608,852 600,835" fill="url(#pocketBlue)"/>
    <polygon points="600,700 1056,760 1056,852 640,852" fill="#0a4fae" opacity="0.35"/>
  </svg>

  <div class="brand-name brand-name--back"><span class="brand-mark"></span>Brightfen<span class="brand-sub">Landscaping</span></div>

  <div class="contact contact--address">
    <div class="contact-row">
      <svg width="7" height="9" viewBox="0 0 7 9"><path d="M3.5 0A3.2 3.2 0 0 0 .3 3.2C.3 5.6 3.5 9 3.5 9s3.2-3.4 3.2-5.8A3.2 3.2 0 0 0 3.5 0zm0 4.5a1.3 1.3 0 1 1 0-2.6 1.3 1.3 0 0 1 0 2.6z" fill="var(--text-dark)"/></svg>
      <span>2245 Alder Creek Road, Unit 7</span>
    </div>
    <div class="contact-indent">Mississauga, Ontario<br>L5T 2B9</div>
  </div>

  <div class="contact contact--lines">
    <div class="contact-row">
      <svg width="8" height="8" viewBox="0 0 8 8"><path d="M1.6 0l1.3 1.9-.8 1c.5 1 1.3 1.8 2.3 2.3l1-.8L8 5.7 7 7.7C3.3 7.5.5 4.7.3 1z" fill="var(--text-dark)"/></svg>
      <span>(647) 392-5180</span>
    </div>
    <div class="contact-row">
      <svg width="8" height="8" viewBox="0 0 8 8"><rect x="0" y="1.5" width="8" height="5" fill="var(--text-dark)"/><path d="M0 1.5l4 2.8 4-2.8" stroke="#fff" stroke-width=".7" fill="none"/></svg>
      <span>info@brightfenlandscaping.example</span>
    </div>
    <div class="contact-row">
      <svg width="8" height="8" viewBox="0 0 8 8"><circle cx="4" cy="4" r="3.6" fill="var(--text-dark)"/></svg>
      <span>www.brightfenlandscaping.example</span>
    </div>
  </div>

  <div class="warranty"><span class="warranty-num">24</span><span class="warranty-words"><span>month</span><span>warranty</span></span></div>

  <div class="brand-name brand-name--front"><span class="brand-mark"></span>Brightfen<span class="brand-sub">Landscaping</span></div>

  <p class="slogan">
    <span class="line-1">The experience you Want</span>
    <span class="line-2">The service you Expect</span>
    <span class="line-3">&amp; The value you Deserve</span>
  </p>
</div>
</body>
</html>
```